Brightline Villas Estepona listings flyer

Brightline Villas Estepona are a specialist estate agency focussed solely on selling modern and contemporary homes.

We need an A4 folded flyer to be designed so that Brightline Villas Estepona can leaflet drop all of the modern homes for sale in our area to generate new instructions / listings. We need to engage with owners of those types of homes by posting this marketing material through their letter boxes in the hope that they see our funky and modern design and decide to call us about our services to sell their home, if for sale.

We would like to see sharp lines and a modern design (see our logo for style and colour scheme), with lots of white spaces and using photos which can blend in to the background to provide a powerful and impacting image to set us aside from any other direct mail leaflets which may be in their post box. It needs to show

* Quality
* Style
* Modern and forward thinking in design and outlook
* Professionalism

Front page
Top:
Logo of Brightline Villas Estepona.
Helping you sell your modern home. It’s all we do!

4 property photos in a grid position

Bottom banner
If you are thinking of selling, read on…

INSIDE LEFT & RIGHT (DOUBLE PAGE POSSIBLY BLANK WHITE BACKGROUND)
Title: Use Brightline Villas Estepona – the specialist modern homes agency to sell your home

We bring an exciting and dynamic mix of modern marketing with good old fashioned service to guarantee only the most qualified clients will be viewing your home (use online marketing image)

Marketing packages include stylish online brochures, professional photography, stunning drone video footage, informative video walk thru’s and unique floor plans (use drone and floor plan images)

Targeted social media campaigns focusing on international clientele actively looking to buy property in southern Spain (use social media image)

Bespoke, powerful advertising packages enable worldwide exposure for both online and traditional channels to market. We can be as discreet or as visible as you want us to be to sell your home

During our 20 years on the Costa del Sol, we have built up an enviable network of collaborating agents meaning you only have to instruct one expert real estate agent, Brightline Villas Estepona, to gain maximum exposure for your home

BACK PAGE

If you want service that matches the value of your home, contact us today for a private, personalised consultation. Brightline Villas Estepona. It’s all we do.

Suite 14
Torrenova Office Park
Calle Los Almendros
Valdemoro, Marbella

Tel: +34 952 418 306
Mobil y Whatsapp: +34 677 342 815
Email: info@brightlinevillasestepona.example
www.brightlinevillasestepona.example

Target Market(s)

Wealthy property owners of contemporary and modern homes who are looking to sell their home

Industry/Entity Type

Real Estate Agent

Font styles to use
Serif
Sans Serif

Colors
606060
e7e7e7
f5f5f5

Requirements
Must have
• Classy, professional, modern design with the ability to stand out from other leaflet drops / direct mail in letter box
Nice to have
• straight lines to border photos
• Maybe extend the lines further than they should so it has the look of an architects plan
• Blend in images to white background in the middle open double page
Should not have
• Lots of different colours

```html
<!DOCTYPE html>
<html lang="en">
<head>
<meta charset="utf-8">
<title>Brightline Villas Estepona – Inside Spread</title>
<link rel="stylesheet" href="https://fonts.googleapis.com/css2?family=Ubuntu:wght@400;700&display=swap">
<style>
  :root {
    --backdrop: #c9c9cb;
    --paper: #ffffff;
    --paper-tint: #f5f5f5;
    --rule: #e7e7e7;
    --ink: #606060;
    --ink-strong: #4a4a4a;
    --sky: #2a66bf;
    --sky-mid: #5d93d8;
    --sky-light: #a9c8ec;
    --facade: #e8ecf0;
    --facade-shade: #cfd6dd;
    --terrace: #d6cfc0;
    --lawn: #8fbf5a;
    --lawn-light: #b9d78e;
  }
  * { margin: 0; padding: 0; box-sizing: border-box; }
  html, body {
    width: 1200px;
    height: 900px;
    overflow: hidden;
    background: var(--backdrop);
    font-family: "Ubuntu", Arial, sans-serif;
  }
  .spread {
    position: absolute;
    left: 240px;
    top: 40px;
    width: 720px;
    height: 820px;
    display: flex;
    background: var(--paper);
    box-shadow: 0 16px 40px rgba(0,0,0,0.18);
  }
  .page {
    position: relative;
    width: 360px;
    height: 820px;
    background: linear-gradient(180deg, var(--paper) 0%, var(--paper) 65%, var(--paper-tint) 100%);
    overflow: hidden;
  }
  .page--right { border-left: 1px solid var(--rule); }

  .page__photo {
    position: absolute;
    left: 0;
    top: 0;
    width: 100%;
  }
  .page__photo::after {
    content: "";
    position: absolute;
    left: 0;
    right: 0;
    bottom: 0;
    height: 32%;
    background: linear-gradient(180deg, rgba(255,255,255,0) 0%, var(--paper) 100%);
  }
  .page__photo--villa {
    height: 300px;
    background: linear-gradient(180deg,
      var(--sky) 0%, var(--sky-mid) 18%, var(--sky-light) 34%,
      var(--facade) 46%, var(--facade-shade) 68%, var(--terrace) 86%, var(--terrace) 100%);
  }
  .page__photo--terrace {
    height: 285px;
    background: linear-gradient(180deg,
      var(--sky) 0%, var(--sky-mid) 8%, var(--sky-light) 16%,
      var(--facade) 26%, var(--facade-shade) 52%, var(--facade) 66%,
      var(--lawn) 72%, var(--lawn-light) 100%);
  }

  .page__copy {
    position: absolute;
    color: var(--ink);
    font-size: 14px;
    line-height: 20px;
    letter-spacing: 0.02em;
    text-align: justify;
  }
  .page--left .page__copy { left: 48px; right: 24px; top: 318px; }
  .page--right .page__copy { left: 66px; right: 38px; top: 296px; }
  .page__copy p + p { margin-top: 20px; }
  .lead-name { font-weight: 700; color: var(--ink-strong); }

  .brand-mark {
    position: absolute;
    bottom: 34px;
    display: flex;
    align-items: center;
    gap: 8px;
    color: var(--ink);
    font-size: 11px;
    font-weight: 700;
    letter-spacing: 0.04em;
    text-transform: uppercase;
  }
  .page--left .brand-mark { left: 48px; }
  .page--right .brand-mark { right: 38px; bottom: 100px; }
  .brand-mark__square {
    width: 12px;
    height: 12px;
    background: var(--ink);
  }
</style>
</head>
<body>
  <main class="spread">
    <section class="page page--left">
      <div class="page__photo page__photo--villa" role="img" aria-label="Photo of a white modern villa with terraces and palm trees under a blue sky, fading into the white page"></div>
      <div class="page__copy">
        <p><span class="lead-name">Use Brightline Villas Estepona</span> – the specialist modern homes agency to sell your home</p>
        <p>We bring an exciting and dynamic mix of modern marketing with good old fashioned service to guarantee only the most qualified clients will be viewing your home.</p>
        <p>Marketing packages include stylish online brochures, professional photography, stunning drone video footage, informative video walk thru’s and unique floor plans</p>
      </div>
      <div class="brand-mark"><span class="brand-mark__square"></span>Brightline Villas Estepona</div>
    </section>
    <section class="page page--right">
      <div class="page__photo page__photo--terrace" role="img" aria-label="Photo of white contemporary apartments with pergolas above a green lawn and pool, fading into the white page"></div>
      <div class="page__copy">
        <p>Targeted social media campaigns focusing on international clientele actively looking to buy property in southern Spain</p>
        <p>Bespoke, powerful advertising packages enable worldwide exposure for both online and traditional channels to market. We can be as discreet or as visible as you want us to be to sell your home</p>
        <p>During our 20 years on the Costa del Sol, we have built up an enviable network of collaborating agents meaning you only have to instruct one expert real estate agent, Brightline Villas Estepona, to gain maximum exposure for your home</p>
      </div>
      <div class="brand-mark"><span class="brand-mark__square"></span>Brightline Villas Estepona</div>
    </section>
  </main>
</body>
</html>
```